The Stone Lantern business cards

Hi
i have attached a photo, this is how i want the front of my business card to look like:
i want the water drop on the right to be orange
and the water drop on the left to be gloss black
"The" and "Pty Ltd." will be in the same orange as the water drop
and "Stone Lantern" will be in white
The background of the logo will be a matte black
on the back of the business card i need the following info:
'The Stone Lantern pty ltd. '
'Plumbing . Drainage . Gas Fitting . Roofing . Jet Blasting . CCTV . '
Also my contact details:
Cal Dreyfus
0418627391
thestonelantern@mailvale.example
Licence# 861027K
Target Market(s)
Strata managers, building managers, the general public
Industry/Entity Type
Business

```html
<!DOCTYPE html>
<html lang="en">
<head>
<meta charset="utf-8">
<title>The Stone Lantern – Business Cards</title>
<link rel="stylesheet" href="https://fonts.googleapis.com/css2?family=Open+Sans:wght@400;600;700&display=swap">
<style>
  :root {
    --backdrop: #d9d4d3;
    --card-black: #232222;
    --band-black: #161515;
    --orange: #f26a1b;
    --white: #f4f2f1;
    --grey-text: #c9c6c5;
  }
  * { box-sizing: border-box; margin: 0; padding: 0; }
  html, body {
    width: 1200px; height: 845px; overflow: hidden;
    background: var(--backdrop);
    font-family: "Open Sans", Arial, sans-serif;
  }
  .sheet {
    width: 1200px; height: 845px;
    display: flex; align-items: center; justify-content: center; gap: 40px;
  }
  .card {
    position: relative;
    width: 540px; height: 330px;
    background: var(--card-black);
    box-shadow: 0 10px 24px rgba(0,0,0,.22);
    overflow: hidden;
  }

  /* Brand lockup */
  .brand { display: flex; align-items: center; }
  .brand-dot { border-radius: 50%; background: var(--orange); flex: none; }
  .brand-text { display: flex; flex-direction: column; align-items: flex-end; }
  .brand-name {
    color: var(--white); font-weight: 700; line-height: 1.05;
    letter-spacing: .5px; white-space: nowrap;
  }
  .brand-suffix { color: var(--orange); font-weight: 400; line-height: 1.1; }

  /* Front */
  .card-front .brand {
    position: absolute; inset: 0; justify-content: center; gap: 22px;
  }
  .card-front .brand-dot { width: 78px; height: 78px; }
  .card-front .brand-name { font-size: 38px; }
  .card-front .brand-suffix { font-size: 18px; margin-top: 2px; }

  /* Back */
  .card-back .top-band {
    position: absolute; left: 0; right: 0; top: 104px; height: 14px;
    background: var(--band-black);
  }
  .card-back .brand { position: absolute; left: 34px; top: 128px; gap: 10px; }
  .card-back .brand-dot { width: 22px; height: 22px; }
  .card-back .brand-name { font-size: 22px; }
  .card-back .brand-suffix { font-size: 11px; }

  .person { position: absolute; left: 34px; top: 196px; }
  .person-name {
    color: var(--white); font-size: 28px; font-weight: 400; letter-spacing: 1px;
    text-transform: uppercase; line-height: 1;
  }
  .person-name strong { font-weight: 700; }
  .person-role { color: var(--orange); font-size: 15px; letter-spacing: 1.5px; margin-top: 2px; }

  .licence {
    position: absolute; right: 34px; top: 232px;
    color: var(--grey-text); font-size: 11px; letter-spacing: .4px;
  }

  .services-band {
    position: absolute; left: 0; right: 0; top: 262px; height: 24px;
    background: var(--band-black);
    display: flex; align-items: center; padding-left: 34px;
    color: var(--grey-text); font-size: 10.5px; letter-spacing: .4px;
  }

  .contacts {
    position: absolute; left: 34px; right: 20px; top: 294px;
    display: flex; align-items: center; gap: 44px;
  }
  .contact { display: flex; align-items: center; gap: 10px; }
  .contact-icon {
    width: 22px; height: 22px; background: var(--orange);
    display: flex; align-items: center; justify-content: center;
  }
  .contact-phone { color: var(--white); font-weight: 700; font-size: 15px; letter-spacing: .5px; }
  .contact-email { color: var(--grey-text); font-size: 13px; }
</style>
</head>
<body>
<main class="sheet">

  <section class="card card-front" aria-label="Business card front">
    <div class="brand">
      <span class="brand-dot"></span>
      <span class="brand-text">
        <span class="brand-name">The Stone Lantern</span>
        <span class="brand-suffix">Pty Ltd</span>
      </span>
    </div>
  </section>

  <section class="card card-back" aria-label="Business card back">
    <div class="top-band"></div>
    <div class="brand">
      <span class="brand-dot"></span>
      <span class="brand-text">
        <span class="brand-name">The Stone Lantern</span>
        <span class="brand-suffix">Pty Ltd</span>
      </span>
    </div>

    <div class="person">
      <p class="person-name">Cal <strong>Dreyfus</strong></p>
      <p class="person-role">plumber</p>
    </div>

    <p class="licence">Licence# 861027K</p>

    <div class="services-band">Plumbing . Drainage . Gas Fitting . Roofing . Jet Blasting . CCTV</div>

    <div class="contacts">
      <div class="contact">
        <span class="contact-icon">
          <svg width="14" height="14" viewBox="0 0 24 24" aria-hidden="true">
            <path fill="#fff" d="M6.6 10.8a15 15 0 0 0 6.6 6.6l2.2-2.2a1 1 0 0 1 1-.25 11.4 11.4 0 0 0 3.6.6 1 1 0 0 1 1 1V20a1 1 0 0 1-1 1A17 17 0 0 1 3 4a1 1 0 0 1 1-1h3.5a1 1 0 0 1 1 1c0 1.250.2 2.45.6 3.6a1 1 0 0 1-.25 1z"/>
          </svg>
        </span>
        <span class="contact-phone">0418627391</span>
      </div>
      <div class="contact">
        <span class="contact-icon">
          <svg width="14" height="14" viewBox="0 0 24 24" aria-hidden="true">
            <rect x="2" y="5" width="20" height="14" fill="#fff"/>
            <path d="M2 5l10 8 10-8" fill="none" stroke="#f26a1b" stroke-width="2"/>
          </svg>
        </span>
        <span class="contact-email">thestonelantern@mailvale.example</span>
      </div>
    </div>
  </section>

</main>
</body>
</html>
```